Venture Capital Investment Firm

We are looking to overhaul our existing website (substantially), with only using the same logos (which we can provide).
We are an investment firm that focuses on making loans to late stage technology companies. Our site should ultimately look like other venture capital firms, and look modern and fresh. We have an existing website www.northvaleloan.com which this will be replacing, although we will be using a lot of the existing written content, and potentially the numbers of pages we will need, we are not wed to anything else. Please feel free to shoot any questions at any time and thank you in advance for your help!
Websites we like as examples:
https://www.tkbrandel.com/
https://www.emberwoodfunds.com/
Target Market(s)
Potential investors who will invest in our firm, as well as potentially companies that are looking to borrow money from us.

```html
<!DOCTYPE html>
<html lang="en">
<head>
<meta charset="utf-8">
<title>Northvale Loan — Home</title>
<link rel="stylesheet" href="https://fonts.googleapis.com/css2?family=Open+Sans:wght@400;600&family=Source+Serif+4:wght@400;700&display=swap">
<style>
  :root {
    --ink: #141414;
    --gold: #d3ae48;
    --gold-bright: #e0b73f;
    --gold-pale: #ead9a6;
    --white: #ffffff;
    --paper: #ffffff;
    --sky-top: #8a939b;
    --sky-mid: #4d5c6b;
    --sky-low: #23313f;
    --overlay: rgba(40, 40, 40, 0.55);
    --serif: "Source Serif 4", Georgia, serif;
    --sans: "Open Sans", Arial, sans-serif;
  }
  * { box-sizing: border-box; margin: 0; padding: 0; }
  html, body { width: 1200px; height: 865px; overflow: hidden; background: var(--paper); }
  .page { position: relative; width: 1200px; height: 865px; overflow: hidden; font-family: var(--sans); }

  .site-header {
    position: absolute; left: 0; top: 0; width: 1200px; height: 88px;
    background: var(--ink);
  }
  .brand {
    position: absolute; left: 189px; top: 28px; display: flex; align-items: center; gap: 12px;
    font-family: var(--serif); font-weight: 400; font-size: 25px; color: var(--gold);
    letter-spacing: 0.5px; white-space: nowrap;
  }
  .brand-dot { width: 22px; height: 22px; border-radius: 50%; background: var(--gold); }
  .main-nav { position: absolute; top: 37px; left: 0; }
  .main-nav a {
    position: absolute; white-space: nowrap; text-decoration: none;
    font-size: 11.5px; font-weight: 600; color: var(--white); letter-spacing: 0.2px;
  }
  .main-nav a.is-active { color: var(--gold-bright); }

  .divider { position: absolute; left: 522px; top: 0; width: 1px; height: 654px; background: rgba(255,255,255,0.22); }

  .hero-photo {
    position: absolute; left: 0; top: 88px; width: 1200px; height: 566px;
    background: linear-gradient(180deg, var(--sky-top) 0%, var(--sky-mid) 45%, var(--sky-low) 100%);
  }
  .hero-card {
    position: absolute; left: 189px; top: 142px; width: 388px; height: 258px;
    background: var(--overlay);
  }
  .hero-photo + .site-header + .divider + .hero .hero-card { top: 142px; }
  .hero { position: absolute; left: 0; top: 88px; width: 1200px; height: 566px; }
  .bracket { position: absolute; border-color: var(--gold); border-style: solid; }
  .bracket-tl { left: 201px; top: 163px; width: 84px; height: 76px; border-width: 5px 0 0 5px; }
  .bracket-br { left: 446px; top: 280px; width: 84px; height: 76px; border-width: 0 5px 5px 0; }
  .hero-title {
    position: absolute; left: 218px; top: 188px; white-space: nowrap;
    font-family: var(--serif); font-weight: 700; font-size: 43px; line-height: 51px; color: var(--white);
  }
  .hero-kicker {
    position: absolute; left: 219px; top: 293px; white-space: nowrap;
    font-family: var(--serif); font-weight: 400; font-size: 22px; color: var(--white); letter-spacing: 0.3px;
  }
  .slider-controls { position: absolute; left: 234px; top: 332px; display: flex; gap: 18px; }

  .intro-panel {
    position: absolute; left: 189px; top: 489px; width: 833px; height: 290px;
    background: var(--gold);
  }
  .intro-illustration {
    position: absolute; left: 44px; top: 73px; width: 94px; height: 147px;
    background: var(--gold-pale); border-radius: 47px 47px 14px 14px;
  }
  .intro-title {
    position: absolute; left: 179px; top: 30px; width: 620px;
    font-family: var(--serif); font-weight: 700; font-size: 26px; line-height: 35px;
    color: var(--white); text-transform: uppercase;
  }
  .intro-copy {
    position: absolute; left: 179px; top: 117px; width: 625px;
    font-size: 10.5px; line-height: 16px; color: var(--white);
  }
  .intro-copy p + p { margin-top: 15px; }

  .services-heading {
    position: absolute; left: 0; top: 804px; width: 1200px; text-align: center;
    font-family: var(--serif); font-weight: 700; font-size: 22px; color: #222;
  }
  .services-mark { position: absolute; left: 594px; top: 842px; width: 12px; height: 12px; border-radius: 50%; background: var(--gold); }
</style>
</head>
<body>
<main class="page">
  <div class="hero-photo" role="img" aria-label="Photo of a businessman on a rooftop balcony overlooking a city skyline"></div>

  <header class="site-header">
    <div class="brand"><span class="brand-dot"></span><span>NORTHVALE LOAN</span></div>
    <nav class="main-nav">
      <a class="is-active" style="left:563px" href="#">HOME</a>
      <a style="left:621px" href="#">STRATEGY</a>
      <a style="left:699px" href="#">ABOUT US</a>
      <a style="left:779px" href="#">TEAM</a>
      <a style="left:834px" href="#">NEWS</a>
      <a style="left:890px" href="#">INVESTORS</a>
      <a style="left:975px" href="#">CONTACT</a>
    </nav>
  </header>

  <div class="divider"></div>

  <section class="hero">
    <div class="hero-card"></div>
    <div class="bracket bracket-tl"></div>
    <div class="bracket bracket-br"></div>
    <h1 class="hero-title">Exceptional<br>Investments,</h1>
    <p class="hero-kicker">EXTRAORDINARY WORLD</p>
    <div class="slider-controls">
      <svg width="22" height="22" viewBox="0 0 22 22" aria-label="Previous slide"><circle cx="11" cy="11" r="10" fill="none" stroke="#fff" stroke-width="1.3"/><path d="M15 11H7M10 8l-3 3 3 3" fill="none" stroke="#fff" stroke-width="1.3"/></svg>
      <svg width="22" height="22" viewBox="0 0 22 22" aria-label="Next slide"><circle cx="11" cy="11" r="10" fill="none" stroke="#fff" stroke-width="1.3"/><path d="M7 11h8M12 8l3 3-3 3" fill="none" stroke="#fff" stroke-width="1.3"/></svg>
    </div>
  </section>

  <section class="intro-panel">
    <div class="intro-illustration" role="img" aria-label="Illustration of a lightbulb with a brain inside"></div>
    <h2 class="intro-title">Finance proven innovation with a different approach</h2>
    <div class="intro-copy">
      <p>Northvale Loan is a private investment firm unique in its dual focus on life science and technology credit opportunities. Our ambidextrous approach to investing reflects a broad recognition and appreciation for the critical role intellectual property plays in the successful commercialization of products. We apply our extensive industry expertise to assess the revenue visibility created by these assets and offer a range of creative financing solutions.</p>
      <p>A pioneer in providing life science structured credit beginning in 2004, the Northvale Loan team was the first to introduce flexible structured credit to the technology sector in 2014. Our team was also early to recognize the potential of "non-core" assets beyond drug royalties, acquiring over $300M of branded generics offering predictable cash flows from large pharmaceutical firms and partnering with entrepreneurial teams to successfully manage these brands.</p>
    </div>
  </section>

  <h2 class="services-heading">Our Services</h2>
  <span class="services-mark"></span>
</main>
</body>
</html>
```